Business Card for Fashion House

We need a business card design for our personalize fashion service for our customers. the business card should reflect reliability, luxury and creativity.
The brand Gravetto is extracted from "Graceful Vetto"; Gravetto provides fashion designs sprinkled with luxury and style tailored for our elite clients character profile.
Gravetto is created for those who embody class and elegance with a passion for style.
Target Market(s)
Affluent Customers
Industry/Entity Type
Fashion
Contact Information for Business Card
Rania Bou Khalil
Fashion Designer
Telephone: +971 5550123
Mobile +971 555987
Emal q@z.com
Website www.gravetto-example.com
Social Media Youtube g+ Facebook Instagram Pin /gravetto
Font styles to use
Other font styles liked:
- Audrey provided
Look and feel
Each slider illustrates characteristics of the customer's brand and the style your logo design should communicate.

```html
<!DOCTYPE html>
<html lang="en">
<head>
<meta charset="utf-8">
<title>Gravetto – Business Card</title>
<link href="https://fonts.googleapis.com/css2?family=Marcellus&family=Lato:wght@400;700&display=swap" rel="stylesheet">
<style>
  :root {
    --stage: #2b2b2b;
    --card-dark: #000000;
    --card-light: #ffffff;
    --ink-light: #ffffff;
    --ink-dark: #111111;
    --ink-muted: #333333;
    --rule: #222222;
  }
  * { box-sizing: border-box; margin: 0; padding: 0; }
  html, body {
    width: 1200px; height: 880px; overflow: hidden;
    background: var(--stage);
  }
  .stage { position: relative; width: 1200px; height: 880px; }
  .card {
    position: absolute; width: 560px; height: 320px;
    border-radius: 26px; overflow: hidden;
    box-shadow: 0 18px 40px rgba(0,0,0,.45);
  }
  .card--back { left: 110px; top: 70px; background: var(--card-dark); color: var(--ink-light); }
  .card--front { left: 530px; top: 470px; background: var(--card-light); color: var(--ink-dark); }

  .wordmark {
    font-family: "Marcellus", serif;
    letter-spacing: .42em;
    text-transform: uppercase;
  }
  .card--back .wordmark {
    position: absolute; left: 0; right: 0; top: 122px;
    text-align: center; font-size: 30px; padding-left: .42em;
  }
  .social-row {
    position: absolute; left: 0; right: 0; top: 198px;
    display: flex; justify-content: center; gap: 10px;
  }
  .social-row span {
    width: 26px; height: 26px; border-radius: 50%;
    border: 2px solid var(--ink-light);
  }

  .card--front .wordmark {
    position: absolute; right: 40px; top: 70px;
    font-size: 28px;
  }
  .front-rule {
    position: absolute; left: 30px; right: 30px; top: 212px;
    border-top: 1.5px solid var(--rule);
  }
  .contact-row {
    position: absolute; left: 30px; right: 30px; top: 228px;
    display: flex; align-items: center;
    font-family: "Lato", sans-serif; font-size: 14px; color: var(--ink-muted);
  }
  .person { width: 170px; }
  .person__name { font-weight: 700; font-size: 16px; color: var(--ink-dark); }
  .person__role { font-size: 14px; margin-top: 2px; }
  .divider { width: 1.5px; height: 46px; background: var(--rule); margin: 0 20px; }
  .contact-list { list-style: none; display: flex; flex-direction: column; gap: 6px; }
  .contact-list li { display: flex; align-items: center; gap: 8px; }
  .contact-list svg { width: 18px; height: 18px; flex: none; }
</style>
</head>
<body>
<main class="stage">
  <section class="card card--back" aria-label="Card back">
    <div class="wordmark">Gravetto</div>
    <div class="social-row" aria-label="Social media profiles">
      <span></span><span></span><span></span><span></span><span></span>
    </div>
  </section>

  <section class="card card--front" aria-label="Card front">
    <div class="wordmark">Gravetto</div>
    <div class="front-rule"></div>
    <div class="contact-row">
      <div class="person">
        <div class="person__name">Rania Bou Khalil</div>
        <div class="person__role">Fashion Designer</div>
      </div>
      <div class="divider"></div>
      <ul class="contact-list">
        <li>
          <svg viewBox="0 0 20 20" aria-hidden="true"><circle cx="10" cy="10" r="9" fill="none" stroke="#111" stroke-width="1.5"/><path d="M6 8c0-1 1-2 4-2s4 1 4 2l-1.5 1-1-1h-3l-1 1z M7 11h6v3H7z" fill="#111"/></svg>
          +971 5550123
        </li>
        <li>
          <svg viewBox="0 0 20 20" aria-hidden="true"><circle cx="10" cy="10" r="9" fill="none" stroke="#111" stroke-width="1.5"/><rect x="7" y="5" width="6" height="10" rx="1" fill="none" stroke="#111" stroke-width="1.4"/></svg>
          +971 555987
        </li>
      </ul>
      <div class="divider"></div>
      <ul class="contact-list">
        <li>
          <svg viewBox="0 0 20 20" aria-hidden="true"><circle cx="10" cy="10" r="9" fill="none" stroke="#111" stroke-width="1.5"/><rect x="5.5" y="7" width="9" height="6.5" fill="none" stroke="#111" stroke-width="1.3"/><path d="M5.5 7l4.5 3.5L14.5 7" fill="none" stroke="#111" stroke-width="1.3"/></svg>
          q@z.com
        </li>
        <li>
          <svg viewBox="0 0 20 20" aria-hidden="true"><circle cx="10" cy="10" r="9" fill="none" stroke="#111" stroke-width="1.5"/><circle cx="10" cy="10" r="4.5" fill="none" stroke="#111" stroke-width="1.2"/><path d="M5.5 10h9M10 5.5c-2 3-2 6 0 9M10 5.5c2 3 2 6 0 9" fill="none" stroke="#111" stroke-width="1"/></svg>
          www.gravetto-example.com
        </li>
      </ul>
    </div>
  </section>
</main>
</body>
</html>
```